Postcard Design

TobysKit connects Golf Pro Shops to consumers and in doing so drives new business to the Golf Course through online sales of Pro Shop Merchandise.

Currently, most Golf Pro Shops don't have an online presence for their retail merchandise (golf balls, shirts, clubs, shoes, etc.). Typically a significant amount of their merchandise is sold at a discounted rate after sitting on the racks for a period of time. We will work with pro-shops to get their surplus merchandise online and sold to local golfers...our catch however is that the course does not ship the merchandise, but rather the purchase goes to the course to pick it up and hopefully book a time to play. We like to market three simple steps: 1)Buy your Gear, 2)Pick up your Gear, 3)Play golf

This postcard is one we want to send to the golf pro-shops to encourage them to sign up for our service. This is what we tell the pro-shop managers:

First – you decide what you want to put online
Second – upload merchandise details to your online store at TobysKit.com
Third – Get paid (automatically) and fill tee times
Obviously it’s a bit more involved than that, but not much. TobysKit has brought the local pro-shop to the online consumer. And with no shipping, the only thing you and your staff will need to do is put aside the sold merchandise until the customer comes to pick it up…and hopefully by now they have also booked a round of golf to play while there. This is an opportunity to not only move the merchandise on your shelves; it’s an opportunity to introduce new golfers to your course…golfers who will return time and again, hopefully with three (or more) of their buddies. TobysKit – Buy Near Your Tee

Also, there is no cost to the pro-shop unless something is sold, then at time of payment thru CoinLane, the transaction is split with x% going to the pro-shop and x% going to TobysKit.

Contact info to include on card:
Instead of "Contact Info" though, maybe something like "Talk to Toby", followed by the info...again, this should feel somewhat casual and personal.

www.tobyskit-demo.com
855-TOBYSKITS (855-862-9754)
info@tobyskit-demo.com

I've uploaded our logo files...sorry, thought I had done that in the original submission. FYI - I want something simple...just something to get the Pro-shop Manager to look at the card and take action/go to our website or send an email.

Target Market(s)

This is meant to go to Golf Pro-Shop merchandising managers

Industry/Entity Type

Business

Font styles to use
Other font styles liked:
• Insignia

Requirements
Must have
• Simple
This should feel like it's coming from Toby himself...more of a personal card.
Should not have
• Not too much emphasis on "golf"...they work at golf-shops, they know what a course looks like! :)

```html
<!DOCTYPE html>
<html lang="en">
<head>
<meta charset="utf-8">
<title>TobysKit Postcard</title>
<link rel="stylesheet" href="https://fonts.googleapis.com/css2?family=Cabin:ital,wght@0,400;0,600;0,700;1,400;1,600;1,700&display=swap">
<style>
  :root {
    --orange: #f07a2a;
    --navy: #173c6e;
    --grey-ring: #dcdcdd;
    --grey-text: #a6a8ab;
    --ink: #111111;
    --paper: #ffffff;
  }
  * { margin: 0; padding: 0; box-sizing: border-box; }
  html, body { width: 1200px; height: 930px; overflow: hidden; background: var(--paper); }
  .postcard {
    position: relative;
    width: 1200px;
    height: 930px;
    overflow: hidden;
    background: var(--paper);
    font-family: "Cabin", "Gill Sans", sans-serif;
  }
  .ring-decoration { position: absolute; left: 0; top: 0; }

  .brand-box {
    position: absolute;
    left: 300px; top: 48px;
    width: 637px; height: 188px;
    border: 1px solid #444;
    background: var(--paper);
  }
  .brand-dot {
    position: absolute;
    left: 20px; top: 34px;
    width: 120px; height: 120px;
    border-radius: 50%;
    background: var(--navy);
  }
  .brand-name {
    position: absolute;
    left: 178px; top: 70px;
    font-size: 40px;
    font-weight: 600;
    letter-spacing: 14px;
    color: var(--orange);
    line-height: 1;
  }
  .brand-tagline {
    position: absolute;
    left: 342px; top: 124px;
    font-size: 15px;
    letter-spacing: 3px;
    color: var(--orange);
  }

  .steps { position: absolute; left: 0; top: 0; }
  .step-label {
    position: absolute;
    top: 398px;
    width: 230px;
    text-align: center;
    font-style: italic;
    font-size: 22px;
    color: var(--navy);
    line-height: 1;
  }
  .step-label.buy { left: 86px; }
  .step-label.pickup { left: 333px; }
  .step-label.play { left: 576px; top: 390px; }
  .step-label .emph { font-size: 46px; font-weight: 700; vertical-align: -4px; }

  .headline {
    position: absolute;
    left: 408px; top: 532px;
    font-size: 96px;
    font-weight: 400;
    color: var(--orange);
    line-height: 1;
    letter-spacing: -1px;
  }
  .headline strong { font-weight: 700; }

  .pitch {
    position: absolute;
    left: 741px; top: 631px;
    width: 440px;
    font-size: 14.5px;
    font-weight: 700;
    font-style: italic;
    color: var(--ink);
    line-height: 1.3;
  }

  .contact-band {
    position: absolute;
    left: 0; top: 830px;
    width: 1200px; height: 100px;
    background: var(--navy);
    display: flex;
    align-items: center;
    justify-content: center;
    gap: 24px;
    color: var(--paper);
    font-size: 22px;
  }
  .contact-band .phone { font-weight: 700; font-size: 26px; }
</style>
</head>
<body>
<main class="postcard">
  <svg class="ring-decoration" width="1200" height="930" viewBox="0 0 1200 930" aria-hidden="true">
    <circle cx="990" cy="560" r="365" fill="var(--grey-ring)"/>
    <circle cx="990" cy="560" r="300" fill="var(--paper)"/>
  </svg>

  <header class="brand-box">
    <span class="brand-dot"></span>
    <span class="brand-name">TobysKit</span>
    <span class="brand-tagline">Buy Near Your Tee...</span>
  </header>

  <svg class="steps" width="1200" height="930" viewBox="0 0 1200 930">
    <defs>
      <radialGradient id="ballTone" cx="50%" cy="45%" r="55%">
        <stop offset="0%" stop-color="#ffffff"/>
        <stop offset="100%" stop-color="#fbd9c0"/>
      </radialGradient>
    </defs>
    <g role="img" aria-label="Golf ball illustration">
      <circle cx="201" cy="423" r="106" fill="url(#ballTone)" stroke="var(--orange)" stroke-width="3"/>
    </g>
    <g role="img" aria-label="Golf ball illustration">
      <circle cx="448" cy="423" r="106" fill="url(#ballTone)" stroke="var(--orange)" stroke-width="3"/>
    </g>
    <g role="img" aria-label="Golf ball illustration">
      <circle cx="691" cy="423" r="106" fill="url(#ballTone)" stroke="var(--orange)" stroke-width="3"/>
    </g>
  </svg>
  <p class="step-label buy">...buy your gear...</p>
  <p class="step-label pickup">...pick up your gear...</p>
  <p class="step-label play">...<span class="emph">play</span> golf...</p>

  <h1 class="headline">“talk to <strong>Toby...”</strong></h1>

  <p class="pitch">TobysKit connects Golf Pro Shops to consumers and in doing so drives new business to the Golf Course through online sales of Pro Shop Merchandise.</p>

  <footer class="contact-band">
    <span class="web">www.tobyskit-demo.com</span>
    <span class="phone">855-TOBYSKITS (855-862-9754)</span>
    <span class="email">info@tobyskit-demo.com</span>
  </footer>
</main>
</body>
</html>
```